Promotional Poster for Music Achievement Program

I need a vertical 11x17 poster designed for a new program called Bright Steps Music Achievement Program. The poster will be displayed in the lesson rooms and lobbies of music schools who use this program. The main headline of the flyer should be "Ask your teacher about Bright Steps" And then the additional text should be "Love your lessons and practice like never before with 10 levels of achievement!" I would like to use the logo on the flyer, which I uploaded here. In terms of artwork/design, I am looking for a fun, but clean feel. The purpose of the program is for students to progress through ten levels of achievement as they climb higher and higher to mastery of their instrument at level 10, so a feel of climbing, leveling up, or advancing would be good. And of course, this is a music program, so any musical artwork involved would make sense. But again - nothing too busy or overwhelming!

Target Market(s)

Parents waiting in the lobby of a music school.

Industry/Entity Type

Promotional

Colors

Designer to choose colors to be used in the design.

Requirements
Must have
• - Bright Steps logo
• - This headline: Ask your teacher about Bright Steps
• - This additional text: Love your lessons and practice like never before with 10 levels of achievement!
Nice to have
• In terms of artwork/design, I am looking for a fun, but clean feel. The purpose of the program is for students to progress through ten levels of achievement as they climb higher and higher to mastery of their instrument at level 10, so a feel of climbing, leveling up, or advancing would be good. And of course, this is a music program, so any musical artwork involved would make sense. But again - nothing too busy or overwhelming!
Should not have
• Should not be too busy.

```html
<!DOCTYPE html>
<html lang="en">
<head>
<meta charset="utf-8">
<title>Bright Steps Music Achievement Program</title>
<link rel="stylesheet" href="https://fonts.googleapis.com/css2?family=Montserrat:wght@500;600;700;800&display=swap">
<style>
  :root {
    --paper: #f7f7f5;
    --ink: #2b2b2b;
    --grey: #6b6b6b;
    --red: #d7283a;
    --lime: #c9dc3c;
    --lime-soft: #e6ef9e;
    --orange: #f2a64a;
    --gold: #f2b63a;
    --yellow: #f7d33a;
    --frame-line: #d6d6d6;
  }
  html, body {
    margin: 0;
    padding: 0;
    width: 991px;
    height: 1200px;
    overflow: hidden;
    background: var(--paper);
    font-family: "Montserrat", Arial, sans-serif;
  }
  .poster {
    position: relative;
    width: 991px;
    height: 1200px;
    background: var(--paper);
    overflow: hidden;
  }
  .light-streak {
    position: absolute;
    left: 560px;
    top: 0;
    width: 260px;
    height: 1200px;
    background: linear-gradient(90deg, rgba(230,239,158,0) 0%, rgba(230,239,158,0.5) 50%, rgba(230,239,158,0) 100%);
  }
  .arch-frame {
    position: absolute;
    left: 106px;
    top: 56px;
    width: 790px;
    height: 1080px;
    border: 2px solid var(--frame-line);
    border-bottom: none;
    border-radius: 80px 80px 0 0;
    box-sizing: border-box;
  }

  /* artwork areas */
  .instrument-cluster {
    position: absolute;
    left: 150px;
    top: 105px;
    width: 265px;
    height: 335px;
    border-radius: 60px 40px 50px 70px;
    background:
      radial-gradient(circle at 65% 25%, rgba(215,40,58,0.55) 0%, rgba(215,40,58,0) 45%),
      radial-gradient(circle at 35% 55%, rgba(201,220,60,0.6) 0%, rgba(201,220,60,0) 45%),
      radial-gradient(circle at 55% 80%, rgba(242,166,74,0.55) 0%, rgba(242,166,74,0) 45%);
  }
  .duet-silhouette {
    position: absolute;
    left: 598px;
    top: 90px;
    width: 170px;
    height: 230px;
    border-radius: 70px 70px 20px 20px;
    background: linear-gradient(180deg, rgba(60,60,60,0.55), rgba(43,43,43,0.8));
  }
  .music-band {
    position: absolute;
    left: 108px;
    top: 670px;
    width: 786px;
    height: 220px;
    border-radius: 60px 60px 0 0;
    background: linear-gradient(180deg, rgba(201,220,60,0) 0%, rgba(201,220,60,0.35) 40%, rgba(201,220,60,0.55) 100%);
  }

  /* headline */
  .headline {
    margin: 0;
    font-weight: 700;
    line-height: 1;
  }
  .headline span {
    position: absolute;
    left: 427px;
    padding: 4px 12px 6px;
    color: var(--ink);
  }
  .word-ask { top: 188px; background: var(--lime); font-size: 48px; }
  .word-your { top: 262px; background: var(--red); color: var(--yellow) !important; font-size: 50px; }
  .word-teacher { top: 330px; background: var(--lime); font-size: 62px; }
  .word-about { top: 418px; background: var(--orange); color: var(--red) !important; font-size: 32px; }

  /* brand */
  .brand {
    position: absolute;
    left: 360px;
    top: 492px;
    display: flex;
    align-items: center;
    gap: 16px;
  }
  .brand-square {
    width: 52px;
    height: 52px;
    background: var(--ink);
  }
  .brand-name {
    font-size: 62px;
    font-weight: 700;
    color: var(--ink);
    letter-spacing: -1px;
    line-height: 1;
  }
  .brand-tagline {
    position: absolute;
    left: 430px;
    top: 570px;
    margin: 0;
    font-size: 21px;
    font-weight: 700;
    color: var(--red);
  }

  .swoosh {
    position: absolute;
    left: 108px;
    top: 850px;
  }

  /* badge */
  .badge {
    position: absolute;
    left: 171px;
    top: 818px;
  }
  .badge-caption {
    position: absolute;
    left: 130px;
    top: 1030px;
    width: 250px;
    margin: 0;
    text-align: center;
    font-weight: 700;
    font-size: 23px;
    line-height: 1.3;
  }
  .badge-caption .levels { color: var(--red); display: block; }
  .badge-caption .achievement { color: var(--ink); display: block; }

  /* promise */
  .promise {
    position: absolute;
    left: 445px;
    top: 938px;
    margin: 0;
    font-weight: 800;
    line-height: 1.12;
  }
  .promise-love { display: block; font-size: 66px; color: var(--red); line-height: 1; margin-bottom: 8px; }
  .promise-lessons { display: block; font-size: 36px; color: var(--red); font-weight: 700; }
  .promise-never { display: block; font-size: 37px; color: var(--grey); font-weight: 600; }
  .promise-never strong { color: var(--ink); font-weight: 800; }
</style>
</head>
<body>
<main class="poster">
  <div class="light-streak"></div>
  <div class="arch-frame"></div>

  <div class="instrument-cluster" role="img" aria-label="Illustration of stacked instruments: records, guitar, drum, trumpet and French horn"></div>
  <div class="duet-silhouette" role="img" aria-label="Silhouette illustration of two young musicians playing cello and guitar"></div>
  <div class="music-band" role="img" aria-label="Soft lime silhouettes of instruments and musical notes"></div>

  <h1 class="headline">
    <span class="word-ask">Ask</span>
    <span class="word-your">Your</span>
    <span class="word-teacher">Teacher</span>
    <span class="word-about">About</span>
  </h1>

  <div class="brand">
    <div class="brand-square"></div>
    <div class="brand-name">Bright Steps</div>
  </div>
  <p class="brand-tagline">MUSIC ACHIEVEMENT PROGRAM</p>

  <svg class="swoosh" width="786" height="70" viewBox="0 0 786 70" aria-hidden="true">
    <path d="M0 42 C 120 18, 260 14, 380 30 C 500 46, 620 62, 786 44" fill="none" stroke="#2b2b2b" stroke-width="9" stroke-linecap="round"/>
  </svg>

  <svg class="badge" width="140" height="200" viewBox="0 0 140 200" aria-hidden="true">
    <polygon points="45,110 95,110 95,195 70,175 45,195" fill="#d7283a"/>
    <circle cx="70" cy="70" r="66" fill="#f2b63a"/>
    <circle cx="70" cy="70" r="53" fill="none" stroke="#f7d33a" stroke-width="4"/>
    <text x="70" y="88" text-anchor="middle" font-family="Montserrat, Arial, sans-serif" font-weight="800" font-size="50" fill="#d7283a">10</text>
  </svg>
  <p class="badge-caption">
    <span class="levels">LEVELS OF</span>
    <span class="achievement">ACHIEVEMENT!</span>
  </p>

  <p class="promise">
    <span class="promise-love">LOVE YOUR</span>
    <span class="promise-lessons">LESSONS &amp; PRACTICE</span>
    <span class="promise-never">LIKE NEVER <strong>BEFORE</strong></span>
  </p>
</main>
</body>
</html>
```